Psychology service brochure

Marketing brochure for a new psychological counselling service.
Our old brochure was too boring and conservative. We are selling our services to GP's, psychiatrists, other health providers and of course potential clients. We'd really like a professional, elegant look that conveys us to be compassionate and conscientious providers of psychological services.
I have included a copy of our old brochure and a copy of the changes we'd like to the text.
Updates
I have included a photo of myself and my business partner. Only the faces are needed, so backgrounds would need to be edited out.
Hello, in consultation with my business partner, we would like
the use of our photos in the brochure please (with backgrounds edited out)
no stock photos of random people
use of abstract or nature/floral motifs suggestive of tranquillity
regards,
Miriam
Target Market(s)
General practitioner doctors, potential clients
Industry/Entity Type
Health
Requirements
Must have
- must include BlairMdITC TT- font for the business name
- must include our signature color Pantone 291 (see attached brochure)
- use of the photos of myself and my business partner (with background edited out please)
- keep use of colours to a minimum, 3 colors maximum, one of which must be Pantone 291
- must include changes to the brochure as outlined in the 'Changes to Pamphlet' document.
Nice to have
- an interesting, eye catching layout.
- interesting use of white spaces
- use of subtle abstract or nature/floral related graphics suggestive of tranquillity
Should not have
- should not include our fee
- stock photos of people

```html
<!DOCTYPE html>
<html lang="en">
<head>
<meta charset="utf-8">
<title>Stillwater Grove Counselling – Brochure Inside Spread</title>
<link href="https://fonts.googleapis.com/css2?family=Didact+Gothic&family=Cinzel:wght@400&display=swap" rel="stylesheet">
<style>
  :root{
    --page-bg:#ffffff;
    --brand-blue:#2b4fa6;
    --brand-blue-mid:#2f7fd0;
    --brand-blue-light:#c6dcf3;
    --sky-top:#dceaf7;
    --sky-bottom:#eef4fa;
    --leaf-brown:#a97a4c;
    --leaf-gold:#d4a86a;
    --body-text:#5a5e66;
    --panel-veil:rgba(240,246,252,0.82);
  }
  *{box-sizing:border-box;margin:0;padding:0}
  html,body{width:1200px;height:900px;overflow:hidden;background:var(--page-bg)}
  body{position:relative;font-family:"Didact Gothic","Century Gothic",sans-serif}

  .spread{
    position:absolute;left:60px;top:57px;width:1087px;height:771px;
    background:linear-gradient(180deg,var(--sky-top) 0%,var(--sky-bottom) 70%,#f2f0ea 100%);
    box-shadow:4px 5px 6px rgba(0,0,0,0.45);
    overflow:hidden;
  }
  .scene-photo{
    position:absolute;left:362px;top:0;width:725px;height:771px;
    background:
      radial-gradient(ellipse 220px 320px at 560px 560px,rgba(190,180,190,0.35),transparent 70%),
      radial-gradient(ellipse 260px 200px at 300px 380px,rgba(212,168,106,0.22),transparent 70%),
      linear-gradient(180deg,#d6e6f5 0%,#e6eff8 55%,#eef2f5 100%);
  }
  .leaf-ground{
    position:absolute;left:0;bottom:0;width:100%;height:32px;
    background:linear-gradient(90deg,var(--leaf-brown),var(--leaf-gold) 30%,var(--leaf-brown) 55%,var(--leaf-gold) 80%,var(--leaf-brown));
    opacity:0.75;
  }
  .panel-veil{
    position:absolute;left:0;top:0;width:362px;height:739px;background:var(--panel-veil);
  }
  .edge-band{
    position:absolute;left:0;top:0;width:48px;height:771px;
    background:linear-gradient(90deg,rgba(47,127,208,0.15) 0%,rgba(47,127,208,0.45) 55%,var(--brand-blue) 100%);
  }

  .column{position:absolute;top:26px;color:var(--body-text);font-size:13.6px;line-height:17.1px}
  .column--first{left:72px;width:262px}
  .column--second{left:416px;width:262px;text-align:justify}
  .column--third{left:776px;width:262px}

  .column h2{font-weight:400;color:var(--brand-blue);font-size:23px;line-height:28px}
  .column .credentials{color:var(--brand-blue);font-size:14px;line-height:16px;margin-bottom:16px}
  .column--third h2{margin-bottom:14px}
  .column p{margin-bottom:17px}

  .business-name{
    position:absolute;left:55px;top:675px;
    font-family:"Cinzel",serif;font-size:29px;letter-spacing:5.4px;
    color:var(--brand-blue-light);white-space:nowrap;
  }
</style>
</head>
<body>
<section class="spread">
  <div class="scene-photo" role="img" aria-label="Soft-focus autumn park scene: a mother and baby sitting among falling leaves under a pale sky"></div>
  <div class="leaf-ground" role="img" aria-label="Strip of autumn leaves on the ground"></div>
  <div class="panel-veil"></div>
  <div class="edge-band" role="img" aria-label="Flowing blue line ornament along the left edge"></div>

  <article class="column column--first">
    <h2>Miriam Halloran<br>Clinical Psychologist</h2>
    <div class="credentials">M.Psych (Clin.) MAPS</div>
    <p>Miriam is a Clinical Psychologist with fifteen years of experience providing a range of psychological services to challenging clients within the public mental health sector including forensic, addiction and dual diagnosis services. She has been employed as a Senior Psychologist in this capacity for the last seven years.</p>
    <p>Miriam is a trained and experienced</p>
    <p>Cognitive Behavioural Therapist and is skilled in treating individuals and groups with a range of mood disorders including anxiety, depres-sion and panic disorder, as well as in helping clients to overcome life issues such as grief and loss, stress management and anger management.</p>
    <p>Miriam trains other mental health cli-nicians and university students in treatment modalities including Motivational Interviewing and Brief Interventions. She has an interest in brain-based research into neuroplasticity and it’s application to cognitive therapy and change.</p>
  </article>

  <article class="column column--second">
    <h2>Rosalind Avery<br>Psychologist</h2>
    <div class="credentials">M.Psych (Clin.) MAPS</div>
    <p>Rosalind is a Psychologist, and with fifteen years experience working in the public health sector, seven as a Senior Psychologist, she is a highly skilled clinician in the areas of mental health, addiction and dual diagnosis.</p>
    <p>She has more recently specialised in working with adolescents but has significant experience treating adults, both individually and in a variety of group programmes. She has also facilitated numerous training events and mentored clinicians in addressing dual diagnosis issues with their clients.</p>
    <p>Rosalind primarily utilises a cognitive behavioural framework, motivational inter-viewing, and has a special interest in working with adolescents who are experiencing develop-mental difficulties, antenatal and post-natal depression/stress, and parenting issues. Additionally Rosalind is skilful working in the areas of grief &amp; loss, life transition and adjustment issues, relationship and interpersonal challenges, and personal development.</p>
  </article>

  <article class="column column--third">
    <h2>Our Fee Structure</h2>
    <p>The practice accepts referrals from self-referring individuals, as well as from health professionals such as GPs, Psychiatrists, and Maternal and Child Health Nurses.</p>
    <p>Medicare rebates are available for clients referred for treatment by their GP.</p>
    <p>There are different tiers of rebates for Psychologists under Medicare, and this is dependent on treatment received (individual, group or pregnancy support counselling), and whether you are treated by a Psychologist or a Clinical Psychologist.</p>
    <p>Please contact us directly to further discuss fees for treatment.</p>
    <p>Fees are paid in full at the end of each session, and a receipt is provided which will allow you to obtain your refund at any Medicare office.</p>
    <p>The practice does not bulk bill at this time, but we anticipate the addition of this facility in the future.</p>
  </article>

  <div class="business-name">Stillwater Grove Counselling</div>
</section>
</body>
</html>
```